The Larkspur Bay Clinic Flyer Design

The Larkspur Bay Clinic is a new company providing Dietetic services for people with gastrointestinal disorders. The main client base would be people suffering from Irritable Bowel Syndrome. IBS is a collection of symptoms which (will be individual to the suffer) including constipation/diarrhoea/abdominal pain or discomfort/bloating/belching/flatulence/stomach gurgling/reflux/nausea/urgency/incomplete emptying/fatigue/headaches. IBS affects approx 30% of the population. Previous treatments have generally been ineffectual and include medication, hypnotherapy, healthy eating.
Recently it has been found that the FODMAP diet (a diet low in fermentable Carbohydrates) has been effective in 75% of sufferers.
The Low FODMAP diet is complex and it is highly recommended that it is undertaken only under the supervision of a suitably qualified dietitian. Treatment is available within the QWR but is usually accessible only following consultation with a Gastroenterologist. Most GP's have never heard of this treatment as the research was only published in 2009 in Australia and is yet to filter through to the general practitioner. The Larkspur Bay Clinic is the only clinic in the UK offering dietetic lead specialist services.
I am a member of the KSL and RWMT (logos provided)
The flyer would be double sided, informing the patient of all the self help steps they could take if they have IBS then recommending that they contact The Larkspur Bay Clinic for specialist advice.
Self Help: Healthy eating, regular meals, good intake of non caffeinated non alcoholic non fizzy drinks, regular exercise, stress management.
The flyer would be left in GP surgeries, Health centres, holistic therapy centres, or through doors.
Majority female aged 20-50, able to pay for private services
Clinic

```html
<!DOCTYPE html>
<html lang="en">
<head>
<meta charset="utf-8">
<title>The Larkspur Bay Clinic – IBS Flyer</title>
<link rel="stylesheet" href="https://fonts.googleapis.com/css2?family=Source+Sans+3:ital,wght@0,400;0,600;0,700;1,700&display=swap">
<style>
  :root {
    --page-bg: #e9e9e9;
    --paper: #ffffff;
    --green-dark: #4f7f2a;
    --green-mid: #7fae45;
    --green-light: #a9c97c;
    --heading-blue: #1d3f78;
    --text: #1a1a1a;
    --cta-green: #1b6e3a;
    --tile-start: #ffffff;
    --tile-end: #c9d6ea;
    --bar-start: #ffffff;
    --bar-mid: #d6ebf3;
    --bar-end: #c9d6ea;
  }
  * { margin: 0; padding: 0; box-sizing: border-box; }
  html, body {
    width: 1200px; height: 1000px; overflow: hidden;
    background: var(--page-bg);
    font-family: "Source Sans 3", "Myriad Pro", Arial, sans-serif;
    color: var(--text);
  }
  .flyer {
    position: absolute; left: 315px; top: 65px;
    width: 612px; height: 862px;
    background: var(--paper);
    box-shadow: 0 4px 18px rgba(0,0,0,.25);
  }
  .band {
    position: absolute; left: 0; width: 100%;
    background: linear-gradient(90deg, var(--green-dark) 0%, var(--green-mid) 30%, var(--green-light) 50%, var(--green-mid) 70%, var(--green-dark) 100%);
  }
  .band--top { top: 0; height: 18px; }
  .band--rule { top: 22px; height: 3px; }
  .band--bottom { bottom: 0; height: 60px; }

  .content { position: absolute; left: 22px; top: 46px; width: 572px; }
  .section-title {
    font-style: italic; font-weight: 700; font-size: 21px;
    color: var(--heading-blue); line-height: 26px; margin-bottom: 7px;
  }
  .section-body { font-size: 14px; line-height: 18px; margin-bottom: 10px; }
  .section-body strong { font-weight: 700; }
  .treatment-list { list-style: none; font-size: 14px; }
  .treatment-list li { line-height: 18px; margin-bottom: 8px; }

  .selfhelp-bar {
    position: absolute; left: 13px; top: 402px; width: 585px; height: 30px;
    background: linear-gradient(90deg, var(--bar-start), var(--bar-mid) 50%, var(--bar-end));
    text-align: center; font-style: italic; font-weight: 700;
    font-size: 17px; line-height: 30px; color: var(--heading-blue);
  }
  .selfhelp-tiles { position: absolute; top: 438px; left: 18px; width: 580px; height: 85px; }
  .tile {
    position: absolute; top: 0; width: 105px; height: 85px;
    background: linear-gradient(90deg, var(--tile-start), var(--tile-end));
    display: flex; align-items: center; justify-content: center;
    text-align: center; font-weight: 700; font-size: 11.5px; line-height: 14px;
  }
  .tile--list { text-align: left; justify-content: flex-start; padding-left: 12px; }

  .cta {
    position: absolute; left: 0; top: 562px; width: 612px;
    text-align: center; color: var(--cta-green);
    font-weight: 700; font-size: 20px; line-height: 25px;
  }
  .contact { position: absolute; left: 118px; top: 688px; font-size: 16px; }
  .care-illustration {
    position: absolute; left: 420px; top: 633px; width: 180px; height: 137px;
    background: radial-gradient(ellipse at center, #f1f1f1 0%, #ffffff 75%);
  }
</style>
</head>
<body>
  <main class="flyer">
    <div class="band band--top"></div>
    <div class="band band--rule"></div>

    <div class="content">
      <h2 class="section-title">Affects</h2>
      <p class="section-body">IBS affects approx 30% of the population.<br>
        Previous treatments have generally been ineffectual and include medication, hypnotherapy, healthy eating.<br>
        Recently it has been found that the FODMAP diet (a diet low in fermentable Carbohydrates) has been effective in75% of sufferers.</p>

      <h2 class="section-title">About FODMAP diet</h2>
      <p class="section-body">Treatment with the <strong>FODMAP diet</strong> is clinically proven to work in up to 75% of patients.<br>
        Results can be seen usually within 1-2 weeks.</p>

      <h2 class="section-title">About the Treatment</h2>
      <ol class="treatment-list">
        <li>(1)&nbsp;1 hr teaching session on the elimination phase, phone and e-mail support.</li>
        <li>(2)&nbsp;1hr appt to teach the reintroduction phase</li>
        <li>(3)&nbsp; Appt to assess nutritional adequacy of the diet.</li>
      </ol>
    </div>

    <div class="selfhelp-bar">Self Help</div>
    <div class="selfhelp-tiles">
      <div class="tile" style="left:0">Healthy<br>eating</div>
      <div class="tile" style="left:121px">Regular<br>meals</div>
      <div class="tile tile--list" style="left:240px">good intakeof<br>non caffeinated<br>non alcoholic<br>non fizzy drinks</div>
      <div class="tile" style="left:357px">Regular<br>exercise</div>
      <div class="tile" style="left:475px">Stress<br>management</div>
    </div>

    <p class="cta">If you are suffering from IRRITABLE BOWEL SYNDROME,<br>Contact us today for Specialist Advice.</p>

    <p class="contact">Contact information : Text goes here</p>

    <div class="care-illustration" role="img" aria-label="Faint line illustration of hands held gently over a stomach"></div>

    <div class="band band--bottom"></div>
  </main>
</body>
</html>
```